SHIELD FROM CLAIMS

I'm virtually ready to launch my site, but I have a number of edits and modifications that need to be implemented. More importantly, I'm always looking to improve my site, particularly now that I am making my proverbial "FIRST IMPRESSION." Thus, I'm willing to see if there is someone who can add creativity and perhaps improve what I already have, particularly on the All Important Front Page.

Need extra days to review

```html
<!DOCTYPE html>
<html lang="en">
<head>
<meta charset="utf-8">
<title>Shield From Claims</title>
<link rel="stylesheet" href="https://fonts.googleapis.com/css2?family=Libre+Baskerville:wght@400;700&family=Arimo:wght@400;700&display=swap">
<style>
:root{
  --navy:#0c1230;
  --navy-deep:#080b1d;
  --teal:#14808f;
  --teal-light:#1a93a3;
  --red:#c4122f;
  --ink:#2b2b2b;
  --muted:#555;
  --paper:#f3f3f4;
  --white:#fff;
  --hero-dark:#1d140e;
  --hero-warm:#6a4a2c;
}
*{box-sizing:border-box;margin:0;padding:0}
html,body{width:1200px;height:5325px;overflow:hidden}
body{position:relative;font-family:"Libre Baskerville",serif;color:var(--ink);background:var(--white)}
.abs{position:absolute}
.star-row{display:flex;gap:10px;justify-content:center;align-items:center}
.star-row svg{display:block}

/* hero */
.hero{position:absolute;left:0;top:0;width:1200px;height:884px;
  background:radial-gradient(ellipse at 62% 30%,#8a6a44 0%,var(--hero-warm) 22%,#3a281a 55%,var(--hero-dark) 100%)}
.hero::after{content:"";position:absolute;inset:0;background:rgba(10,6,3,.35)}
.hero > *{z-index:1}
.topbar{position:absolute;left:0;top:0;width:1200px;height:83px;background:rgba(0,0,0,.45);border-bottom:1px solid rgba(255,255,255,.15);display:flex;color:#d9d2c8;font-size:14px}
.topbar .cell{display:flex;align-items:center;gap:14px;border-right:1px solid rgba(255,255,255,.15);padding-left:110px;height:100%}
.topbar .addr{width:430px;font-size:12.5px;line-height:1.6}
.topbar .ph1{width:275px;padding-left:50px;font-size:17px}
.topbar .ph2{width:290px;padding-left:52px;font-size:17px}
.topbar .menu{flex:1;border:none;justify-content:center;padding:0}
.brand-mark{position:absolute;left:525px;top:198px;width:150px;height:150px;border-radius:50%;background:var(--red);border:6px solid var(--white);display:flex;align-items:center;justify-content:center;text-align:center;color:var(--white);font-size:15px;font-weight:700;line-height:1.3}
.hero h1{position:absolute;top:370px;left:0;width:1200px;text-align:center;color:var(--white);font-size:36px;font-weight:700;letter-spacing:1px}
.hero .star-row{position:absolute;top:448px;left:0;width:1200px}
.hero h2{position:absolute;top:565px;left:0;width:1200px;text-align:center;color:var(--white);font-weight:400;font-size:25px;letter-spacing:2px}
.hero p{position:absolute;top:618px;left:132px;width:936px;text-align:center;color:#d9d2c8;font-size:15px;line-height:34px}
.btn{display:inline-flex;align-items:center;justify-content:center;font-size:13px;letter-spacing:.5px;text-transform:uppercase}
.btn-teal{background:var(--teal);color:var(--white)}
.btn-white{background:var(--white);color:var(--navy)}
.hero .b1{position:absolute;left:374px;top:785px;width:281px;height:53px}
.hero .b2{position:absolute;left:681px;top:785px;width:160px;height:53px}

/* about */
.about-title{position:absolute;top:926px;left:0;width:1200px;text-align:center;color:var(--navy);font-size:25px;letter-spacing:1.5px}
.about-pill{position:absolute;left:110px;top:987px;width:978px;height:194px;border:2px solid #7fbfc8;border-radius:97px;background:var(--white)}
.about-pill .mark{position:absolute;left:20px;top:20px;width:150px;height:150px;border-radius:50%;background:var(--red);border:5px solid var(--navy);display:flex;align-items:center;justify-content:center;text-align:center;color:var(--white);font-weight:700;font-size:14px;line-height:1.3}
.about-pill .txt{position:absolute;left:196px;top:28px;width:760px;font-family:"Arimo",sans-serif;font-size:17px;line-height:31px;color:#222}
.about-pill .t{color:var(--teal)}
.about-pill .r{color:var(--red);font-family:"Libre Baskerville",serif;font-size:14.5px;margin-top:10px;display:block}
.about-stars{position:absolute;top:1168px;left:0;width:1200px}

.photo{position:absolute}
.ph-money{left:110px;top:1253px;width:475px;height:292px;background:linear-gradient(120deg,#c9c4b2,#9aa69a 40%,#c7a76a 75%,#6b7b6c)}
.story-a{position:absolute;left:630px;top:1290px;width:444px;font-size:14.5px;line-height:32.5px;color:#333}
.rule{position:absolute;width:96px;height:2px;background:var(--teal)}
.story-b{position:absolute;left:110px;top:1610px;width:462px;font-size:14.5px;line-height:30.5px;color:#333}
.story-b p+p{margin-top:29px}
.story-b .em{font-size:16px;letter-spacing:.5px;color:var(--navy)}
.ph-lawyer{left:613px;top:1604px;width:475px;height:540px;background:linear-gradient(160deg,#3c2a1d,#1e150f 55%,#0d0a08)}
.quote{position:absolute;left:645px;top:1990px;width:420px;color:var(--white)}
.quote .star-row{justify-content:flex-start;margin-left:150px;margin-bottom:14px}
.quote .q{font-size:24px;line-height:31px}
.quote .by{position:absolute;left:210px;top:118px;font-size:14px;color:#ddd}
.quote .by::before{content:"";display:inline-block;width:48px;height:1px;background:#ddd;vertical-align:middle;margin-right:12px}
.quote .mark{position:absolute;right:-10px;top:70px}

/* contact band */
.band{position:absolute;left:0;top:2226px;width:1200px;height:174px;background:linear-gradient(90deg,#0f1a33,#16273f 50%,#0c1428)}
.band h3{position:absolute;left:116px;top:72px;color:var(--white);font-weight:400;font-size:24px;letter-spacing:1px}
.band .btn{position:absolute;left:737px;top:60px;width:308px;height:56px;background:var(--teal-light);color:var(--white)}

/* services */
.services{position:absolute;left:0;top:2400px;width:1200px;height:1778px;background:var(--paper)}
.services .star-row{position:absolute;top:40px;left:0;width:1200px}
.services h2{position:absolute;top:80px;left:0;width:1200px;text-align:center;color:var(--navy);font-weight:400;font-size:25px;letter-spacing:1.5px}
.services .lead{position:absolute;top:131px;left:0;width:1200px;text-align:center;font-size:18px;line-height:36px;color:#333}
.services .lead b{color:var(--teal);font-weight:400;font-size:21px}
.card{position:absolute;width:458px;background:var(--white);box-shadow:0 2px 10px rgba(0,0,0,.12);padding:13px}
.card .img{height:279px;position:relative}
.card .img .btn{position:absolute;right:0;bottom:0;width:156px;height:40px;background:var(--teal);color:var(--white)}
.card h4{font-size:14.5px;font-weight:400;color:#111;letter-spacing:.5px;margin:26px 0 20px 10px}
.card p{font-size:13px;line-height:26px;color:#555;margin:0 10px}
.c1{left:114px;top:237px;height:498px}.c2{left:628px;top:237px;height:498px}
.c3{left:114px;top:774px;height:456px}.c4{left:628px;top:774px;height:456px}
.c5{left:114px;top:1267px;height:443px}.c6{left:628px;top:1267px;height:443px}
.i1{background:linear-gradient(135deg,#6c6f78,#c9b49c 55%,#3b3d45)}
.i2{background:linear-gradient(135deg,#3a1a0c,#8a4a22 50%,#2a150a)}
.i3{background:linear-gradient(135deg,#d9c8a6,#9b8565 55%,#3a2e22)}
.i4{background:linear-gradient(135deg,#1f2a3a,#a9a9a9 60%,#e1e1e1)}
.i5{background:linear-gradient(135deg,#d7b7c4,#8f8a7a 50%,#d3c3a4)}
.i6{background:linear-gradient(135deg,#0e2236,#2a4a5f 50%,#8c6a3a)}

/* faq */
.faq-title{position:absolute;top:4240px;left:0;width:1200px;text-align:center;color:#111;font-weight:400;font-size:25px;letter-spacing:1.5px}
.faq{position:absolute;left:227px;width:743px;border:1px solid #e1e1e1;background:var(--white);font-size:15px;color:#222}
.faq .row{display:flex;align-items:center;height:62px;padding:0 18px;gap:18px}
.faq .row span{flex:1}
.faq.open{background:#f2f2f3}
.faq.open .row span{color:var(--teal);line-height:26px}
.faq .ans{padding:0 20px 22px 64px;font-size:13px;line-height:26px;color:#444}
.f1{top:4318px}.f2{top:4403px}.f3{top:4489px}.f4{top:4568px}.f5{top:4751px}
.f4 .row{height:84px}

/* footer */
.footer{position:absolute;left:0;top:4925px;width:1200px;height:400px;background:var(--navy-deep);color:#ccc}
.footer .mark{position:absolute;left:530px;top:-2px;width:140px;height:140px;border-radius:50%;background:var(--red);border:5px solid var(--white);display:flex;align-items:center;justify-content:center;text-align:center;color:var(--white);font-weight:700;font-size:14px;line-height:1.3}
.footer nav{position:absolute;top:148px;left:110px;width:980px;display:flex;justify-content:space-between;align-items:center;font-size:17px;color:#ddd}
.footer nav i{width:6px;height:6px;border-radius:50%;border:1px solid #777;display:block}
.footer .addr{position:absolute;left:110px;top:232px;display:flex;gap:26px;align-items:center;font-size:13.5px;line-height:22px;letter-spacing:.5px}
.footer .social{position:absolute;left:541px;top:238px;display:flex;gap:22px}
.footer .social i{width:36px;height:36px;border-radius:50%;background:#e8e8e8;display:block}
.footer .phones{position:absolute;left:780px;top:240px;display:flex;gap:18px;align-items:center;font-size:15px}
.footer .copy{position:absolute;top:335px;left:0;width:1200px;text-align:center;font-size:11px;color:#777}
</style>
</head>
<body>

<header class="hero">
  <div class="topbar">
    <div class="cell addr">
      <svg width="18" height="24" viewBox="0 0 18 24"><path d="M9 0a9 9 0 0 0-9 9c0 7 9 15 9 15s9-8 9-15a9 9 0 0 0-9-9zm0 12.5A3.5 3.5 0 1 1 9 5.5a3.5 3.5 0 0 1 0 7z" fill="#d9d2c8"/></svg>
      <span>4780 West Canyon Rd., Suite<br>210 Mesa Verde, Arizona 85099</span>
    </div>
    <div class="cell ph1">
      <svg width="20" height="20" viewBox="0 0 24 24"><path d="M6.6 10.8a15 15 0 0 0 6.6 6.6l2.2-2.2a1 1 0 0 1 1-.25 11.4 11.4 0 0 0 3.6.57 1 1 0 0 1 1 1V20a1 1 0 0 1-1 1A17 17 0 0 1 3 4a1 1 0 0 1 1-1h3.5a1 1 0 0 1 1 1c0 1.25.2 2.45.57 3.57a1 1 0 0 1-.25 1z" fill="#d9d2c8"/></svg>
      <span>480.555.0172</span>
    </div>
    <div class="cell ph2">
      <svg width="20" height="20" viewBox="0 0 24 24"><path d="M6.6 10.8a15 15 0 0 0 6.6 6.6l2.2-2.2a1 1 0 0 1 1-.25 11.4 11.4 0 0 0 3.6.57 1 1 0 0 1 1 1V20a1 1 0 0 1-1 1A17 17 0 0 1 3 4a1 1 0 0 1 1-1h3.5a1 1 0 0 1 1 1c0 1.25.2 2.45.57 3.57a1 1 0 0 1-.25 1z" fill="#d9d2c8"/></svg>
      <span>800.555.0148</span>
    </div>
    <div class="cell menu">
      <svg width="22" height="18" viewBox="0 0 22 18"><rect width="22" height="3" fill="#ddd"/><rect y="7.5" width="22" height="3" fill="#ddd"/><rect y="15" width="22" height="3" fill="#ddd"/></svg>
    </div>
  </div>
  <div role="img" aria-label="Courtroom scene in warm low light" style="position:absolute;inset:83px 0 0 0"></div>
  <div class="brand-mark">Shield<br>From<br>Claims</div>
  <h1>SHIELD FROM CLAIMS</h1>
  <div class="star-row">
    <svg width="30" height="30" viewBox="0 0 24 24"><path d="M12 2l3 7h7l-5.6 4.3 2.1 7.2L12 16.3 5.5 20.5l2.1-7.2L2 9h7z" fill="#fff"/></svg>
    <svg width="34" height="34" viewBox="0 0 24 24" style="margin-top:16px"><path d="M12 2l3 7h7l-5.6 4.3 2.1 7.2L12 16.3 5.5 20.5l2.1-7.2L2 9h7z" fill="#fff"/></svg>
    <svg width="30" height="30" viewBox="0 0 24 24"><path d="M12 2l3 7h7l-5.6 4.3 2.1 7.2L12 16.3 5.5 20.5l2.1-7.2L2 9h7z" fill="#fff"/></svg>
  </div>
  <h2>BUSINESS OWNERS:</h2>
  <p>Shield From Claims (SFC) is an extremely affordable legal service plan (as little as $8.00 per month) that INSULATES business owners from unwarranted LEGAL CLAIMS and expensive LAWSUITS. Our plan uses local, experienced, quality attorneys who focus on PROBLEM PREVENTION using proprietary tools available only to SFC members. Contact us for a free consultation and receive a FREE OVERVIEW of your business to see if you are truly insulated from legal claims.</p>
  <a class="btn btn-teal b1">Schedule Free Consultation</a>
  <a class="btn btn-white b2">Learn More</a>
</header>

<h2 class="about-title">ABOUT US</h2>
<div class="about-pill">
  <div class="mark">Shield<br>From<br>Claims</div>
  <div class="txt">
    <span class="t">SFC</span> is a group of attorney and legal assistants with many years of experience in litigation, who are devoted to <span class="t">PREVENTING LEGAL CLAIMS</span> and <span class="t">COSTLY LAWSUITS</span> through a variety of <span class="t">FREE</span> and <span class="t">VERY AFFORDABLE</span> services described below.
    <span class="r">OUR UNIQUE SERVICE PLAN MAKES IT POSSIBLE FOR US TO STOP THE CLAIMS.</span>
  </div>
</div>
<div class="star-row about-stars">
  <svg width="20" height="20" viewBox="0 0 24 24"><path d="M12 2l3 7h7l-5.6 4.3 2.1 7.2L12 16.3 5.5 20.5l2.1-7.2L2 9h7z" fill="var(--teal)"/></svg>
  <svg width="22" height="22" viewBox="0 0 24 24" style="margin-top:10px"><path d="M12 2l3 7h7l-5.6 4.3 2.1 7.2L12 16.3 5.5 20.5l2.1-7.2L2 9h7z" fill="var(--teal)"/></svg>
  <svg width="20" height="20" viewBox="0 0 24 24"><path d="M12 2l3 7h7l-5.6 4.3 2.1 7.2L12 16.3 5.5 20.5l2.1-7.2L2 9h7z" fill="var(--teal)"/></svg>
</div>

<div class="photo ph-money" role="img" aria-label="Close-up of a banknote portrait wearing a face mask"></div>
<p class="story-a">A homebuilding company was sued by a former employee who claimed to have been promised a more favorable sales area, which claim was disputed by the homebuilder. There was no evidence that such a promise had been made, other than the plaintiff's oral testimony. The company had the case dismissed, but spent <b>$10,000</b> defending the case.</p>
<div class="rule" style="left:630px;top:1503px"></div>

<div class="story-b">
  <p>And even though it was awarded its attorney's fees, the plaintiff proved uncollectible. Had the company been an <b>SFC</b> member, the case likely would never have been filed. Call for your <b>FREE CONSULTATION</b> and let us show you why the plaintiff likely would not have found a contingency attorney (as was the case) or been able to pay an attorney on an hourly basis. In short, by using <b>SFC's</b> services, the plaintiff's claim would not have been filed.</p>
  <p>In our vast experience with commercial litigation, we believe that a very large percentage of litigation cases hinge on "he said / she said" issues. By using SFC's services, we believe we can <b>INSULATE</b> you and your business from all such issues, which will <b>MINIMIZE</b> your <span class="em">EXPOSURE to LEGAL CLAIMS and LAWSUITS</span></p>
</div>
<div class="rule" style="left:110px;top:2134px"></div>

<div class="photo ph-lawyer" role="img" aria-label="Attorney in a robe on the phone in a library office"></div>
<div class="quote">
  <div class="star-row">
    <svg width="16" height="16" viewBox="0 0 24 24"><path d="M12 2l3 7h7l-5.6 4.3 2.1 7.2L12 16.3 5.5 20.5l2.1-7.2L2 9h7z" fill="var(--teal-light)"/></svg>
    <svg width="18" height="18" viewBox="0 0 24 24" style="margin-top:8px"><path d="M12 2l3 7h7l-5.6 4.3 2.1 7.2L12 16.3 5.5 20.5l2.1-7.2L2 9h7z" fill="var(--teal-light)"/></svg>
    <svg width="16" height="16" viewBox="0 0 24 24"><path d="M12 2l3 7h7l-5.6 4.3 2.1 7.2L12 16.3 5.5 20.5l2.1-7.2L2 9h7z" fill="var(--teal-light)"/></svg>
  </div>
  <div class="q">An OUNCE of PREVENTION<br>is worth a POUND of CURE.</div>
  <svg class="mark" width="42" height="34" viewBox="0 0 42 34"><circle cx="10" cy="22" r="9" fill="var(--teal-light)"/><path d="M4 20 Q6 4 18 0 Q10 8 12 16z" fill="var(--teal-light)"/><circle cx="31" cy="22" r="9" fill="var(--teal-light)"/><path d="M25 20 Q27 4 39 0 Q31 8 33 16z" fill="var(--teal-light)"/></svg>
  <div class="by">Old Proverb</div>
</div>

<section class="band">
  <h3>CONTACT US FOR A FREE CONSULTATION</h3>
  <a class="btn">Schedule Free Consulation</a>
</section>

<section class="services">
  <div class="star-row">
    <svg width="20" height="20" viewBox="0 0 24 24"><path d="M12 2l3 7h7l-5.6 4.3 2.1 7.2L12 16.3 5.5 20.5l2.1-7.2L2 9h7z" fill="var(--teal)"/></svg>
    <svg width="22" height="22" viewBox="0 0 24 24" style="margin-top:-10px"><path d="M12 2l3 7h7l-5.6 4.3 2.1 7.2L12 16.3 5.5 20.5l2.1-7.2L2 9h7z" fill="var(--teal)"/></svg>
    <svg width="20" height="20" viewBox="0 0 24 24"><path d="M12 2l3 7h7l-5.6 4.3 2.1 7.2L12 16.3 5.5 20.5l2.1-7.2L2 9h7z" fill="var(--teal)"/></svg>
  </div>
  <h2>OUR SERVICES</h2>
  <p class="lead">The price for a membership is a ridiculously low &nbsp;<b>$9.95 PER WEEK.</b> We believe<br>that this fee is very affordable. So what is it? Membership includes the following:</p>

  <article class="card c1">
    <div class="img i1" role="img" aria-label="Two business people shaking hands over a desk"><a class="btn">Learn More</a></div>
    <h4>FREE INITIAL CONSULTATION</h4>
    <p>As a prospective Shield From Claims ("SFC") member, we urge you to schedule an initial consultation with us – at no charge – where we will go over each of the services in detail, and offer an overview of your business formation at no charge.</p>
  </article>
  <article class="card c2">
    <div class="img i2" role="img" aria-label="Gavel resting beside a signed document"></div>
    <h4>PROPRIETARY CONTRACT LANGUAGE</h4>
    <p>SFC members are entitled to incorporate exclusive proprietary contract language in their contracts, work orders, and other written agreements in their business, that MINIMIZES EXPOSURE to legal claims against your business.</p>
  </article>
  <article class="card c3">
    <div class="img i3" role="img" aria-label="Fountain pen lying on an open book"></div>
    <h4>FREE CONSULTATION</h4>
    <p>SFC members can call their local SFC Attorney any time, and be given a 30 minute consultation, free of charge, once per month. The value of this cannot be overstated and easily pays for the membership - many times over.</p>
  </article>
  <article class="card c4">
    <div class="img i4" role="img" aria-label="Attorney in a suit signing papers"></div>
    <h4>FREE ATTORNEY LETTERS</h4>
    <p>In addition to free monthly consultations, SFC members can have their local SFC Attorney send out a letter regarding their business, once per month, at no charge.</p>
  </article>
  <article class="card c5">
    <div class="img i5" role="img" aria-label="Gavel on top of scattered banknotes"></div>
    <h4>LITIGATION DISCOUNTS</h4>
    <p>SFC members who use the Proprietary Contract Language described above are given considerable discounts, including flat fee discounts, in the event of defensive litigation.</p>
  </article>
  <article class="card c6">
    <div class="img i6" role="img" aria-label="Gavel and scales of justice on a dark desk"></div>
    <h4>COLLECTIONS</h4>
    <p>SFC members can have their SFC Attorney pursue collection claims on a contingency fee basis, provided the claim is based on a contract.</p>
  </article>
</section>

<h2 class="faq-title">FREQUENTLY ASKED QUESTIONS</h2>
<div class="faq f1"><div class="row"><svg width="22" height="22" viewBox="0 0 22 22"><circle cx="11" cy="11" r="11" fill="var(--teal)"/><text x="11" y="16" text-anchor="middle" font-size="14" font-weight="700" fill="#fff" font-family="Arimo,sans-serif">?</text></svg><span>Why should I be concerned about legal claims?</span><svg width="14" height="14"><path d="M7 0v14M0 7h14" stroke="#bbb"/></svg></div></div>
<div class="faq f2"><div class="row"><svg width="22" height="22" viewBox="0 0 22 22"><circle cx="11" cy="11" r="11" fill="var(--teal)"/><text x="11" y="16" text-anchor="middle" font-size="14" font-weight="700" fill="#fff" font-family="Arimo,sans-serif">?</text></svg><span>Provide more details about the value of SFC's contract language.</span><svg width="14" height="14"><path d="M7 0v14M0 7h14" stroke="#bbb"/></svg></div></div>
<div class="faq f3"><div class="row"><svg width="22" height="22" viewBox="0 0 22 22"><circle cx="11" cy="11" r="11" fill="var(--teal)"/><text x="11" y="16" text-anchor="middle" font-size="14" font-weight="700" fill="#fff" font-family="Arimo,sans-serif">?</text></svg><span>What does an SFC membership cost?</span><svg width="14" height="14"><path d="M7 0v14M0 7h14" stroke="#bbb"/></svg></div></div>
<div class="faq f4 open"><div class="row"><svg width="22" height="22" viewBox="0 0 22 22"><circle cx="11" cy="11" r="11" fill="var(--teal)"/><text x="11" y="16" text-anchor="middle" font-size="14" font-weight="700" fill="#fff" font-family="Arimo,sans-serif">?</text></svg><span>If I'm a contractor, for example, how can an SFC membership<br>minimize legal claims against my business?</span><svg width="14" height="14"><path d="M0 7h14" stroke="#bbb"/></svg></div>
  <p class="ans">Lorem ipsum dolor sit amet, consectetur adipiscing elit. Suspendisse varius enim in eros elementum tristique. Duis cursus, mi quis viverra ornare,</p></div>
<div class="faq f5"><div class="row"><svg width="22" height="22" viewBox="0 0 22 22"><circle cx="11" cy="11" r="11" fill="var(--teal)"/><text x="11" y="16" text-anchor="middle" font-size="14" font-weight="700" fill="#fff" font-family="Arimo,sans-serif">?</text></svg><span>Do you have a Referral Program?</span><svg width="14" height="14"><path d="M7 0v14M0 7h14" stroke="#bbb"/></svg></div></div>

<footer class="footer">
  <div class="mark">Shield<br>From<br>Claims</div>
  <nav>
    <a>Home</a><i></i><a>About</a><i></i><a>Services</a><i></i><a>Faq</a><i></i><a>Contact Us</a><i></i><a>Terms Of Service</a><i></i><a>Privacy Policy</a>
  </nav>
  <div class="addr">
    <svg width="26" height="34" viewBox="0 0 18 24"><path d="M9 0a9 9 0 0 0-9 9c0 7 9 15 9 15s9-8 9-15a9 9 0 0 0-9-9zm0 12.5A3.5 3.5 0 1 1 9 5.5a3.5 3.5 0 0 1 0 7z" fill="var(--teal-light)"/></svg>
    <span>4780 WEST CANYON RD., SUITE 210<br>MESA VERDE, ARIZONA 85099</span>
  </div>
  <div class="social"><i></i><i></i><i></i></div>
  <div class="phones">
    <svg width="26" height="26" viewBox="0 0 24 24"><path d="M6.6 10.8a15 15 0 0 0 6.6 6.6l2.2-2.2a1 1 0 0 1 1-.25 11.4 11.4 0 0 0 3.6.57 1 1 0 0 1 1 1V20a1 1 0 0 1-1 1A17 17 0 0 1 3 4a1 1 0 0 1 1-1h3.5a1 1 0 0 1 1 1c0 1.25.2 2.45.57 3.57a1 1 0 0 1-.25 1z" fill="var(--teal-light)"/></svg>
    <span>480.555.0172 / (800) 555-0193</span>
  </div>
  <p class="copy">2023 © All rights reserved by shieldfromclaims.com</p>
</footer>

</body>
</html>
```